Label for Skincare Brand

"Fernleigh Vale Organics" - organic skincare brand
I need a label designed for my organic skincare brand. I have attached pics of brands I like, to give you an idea of style. I would like something minimal although some colour might work. Colours I like are pale blush pink and aqua. I would like a clean, minimalistic modern yet elegant label. Please look at the samples because they demonstrate the style I look for in a label. It is okay to add a graphical element into the design as long as it enhances or add value to the design.
We do not have a logo yet, so I'd appreciate if you could create a simple type logo for Fernleigh Vale Organics similar to the examples attached.
Please can you do two different sizes: one cream jar and one serum bottle. Both will contain the same information.
___________________________________________________
1. Cream Jar (label size 42 x 190 mm) (clear glass with aluminium lid)
2. Serum Bottle (label size 50 x 110 mm) (clear glass with black pump)
FRONT SIDE:
Fernleigh Vale Organics
Nine Moons
Ultimate Anti-Aging Cream
For Dry & Mature Skin
Organic & Palm Oil-Free
100 ml.
BACK SIDE:
Nine Moons Ultimate Anti-Aging Cream
An effective Day Cream that harnesses the best of science to target the signs of aging. The main active ingredient is R58, a patented noncomedogenic lipid complex, carefully engineered from botanically-sourced lipids. It is composed of a variety of lipid types which are carefully combined in the same ratio as those found on healthy young skin of an average 22 year old.
Directions:
Apply to clean skin morning and night.
Ingredients:
Aloe Vera Leaf Juice, Cocos Nucifera Oil, Butyrospermum Parkii Butter, Jojoba Oil/Macadamia Seed Oil Esters (and) Squalene (and) Phytosteryl Macadamiate (and) Phytosterols, Potassium Olivoyl Hydrolyzed Oat Protein (and) Cetearyl Alcohol (and) Glyceryl Oleate (and) Glyceryl Stearat, Benzyl Alcohol, Dehydroacetic Acid.
Fernleigh Vale Organics
6/3 Kelmora Street North, Wahroonga, NSW 2076
www.fernleighvaleorganics.com.au
Any questions, please just ask away. Thank you.

```html
<!DOCTYPE html>
<html lang="en">
<head>
<meta charset="utf-8">
<title>Fernleigh Vale Organics – Ultimate Anti-Aging Cream Labels</title>
<link rel="stylesheet" href="https://fonts.googleapis.com/css2?family=Libre+Baskerville&family=Arimo:ital,wght@0,400;1,400;1,700&display=swap">
<style>
  :root {
    --page-bg: #dce9ee;
    --label-bg: #ffffff;
    --ink: #2a2a2a;
    --ink-soft: #4a4a4a;
    --rule: #3a3a3a;
    --edge: #c9d3d7;
  }
  * { margin: 0; padding: 0; box-sizing: border-box; }
  html, body {
    width: 1200px;
    height: 1200px;
    overflow: hidden;
    background: var(--page-bg);
  }
  .canvas {
    position: relative;
    width: 1200px;
    height: 1200px;
  }
  .label {
    position: absolute;
    background: var(--label-bg);
    border: 1px solid var(--edge);
    color: var(--ink);
  }
  .brand-name {
    position: absolute;
    font-family: "Libre Baskerville", serif;
    font-weight: 400;
    text-transform: uppercase;
    line-height: 1.05;
    letter-spacing: 0.01em;
  }
  .rule {
    position: absolute;
    height: 0;
    border-top: 1.5px solid var(--rule);
  }
  .variant {
    position: absolute;
    font-family: "Arimo", sans-serif;
    color: var(--ink-soft);
  }
  .product-name {
    position: absolute;
    font-family: "Arimo", sans-serif;
    writing-mode: vertical-rl;
    transform: rotate(180deg);
    white-space: nowrap;
    color: var(--ink);
  }
  .details {
    position: absolute;
    font-family: "Arimo", sans-serif;
    font-style: italic;
    line-height: 1.3;
    color: var(--ink);
  }
  .details .volume {
    font-weight: 700;
    margin-top: 0.45em;
  }

  /* Serum bottle label */
  .bottle-label { left: 190px; top: 346px; width: 380px; height: 507px; }
  .bottle-label .brand-name { left: 18px; top: 34px; font-size: 28px; }
  .bottle-label .rule { left: 18px; right: 0; top: 108px; }
  .bottle-label .variant { left: 18px; top: 118px; font-size: 18px; }
  .bottle-label .product-name { left: 322px; top: 150px; font-size: 23px; }
  .bottle-label .details { left: 18px; top: 320px; font-size: 19px; }

  /* Carton front panel */
  .carton-panel { left: 680px; top: 196px; width: 300px; height: 808px; }
  .carton-panel .brand-name { left: 49px; top: 60px; font-size: 24px; }
  .carton-panel .rule.top-rule { left: 49px; width: 217px; top: 118px; }
  .carton-panel .variant { left: 49px; top: 128px; font-size: 14px; }
  .carton-panel .product-name { left: 34px; top: 440px; font-size: 25px; }
  .carton-panel .rule.bottom-rule { left: 71px; right: 0; top: 704px; }
  .carton-panel .details { left: 71px; top: 718px; font-size: 14px; }
</style>
</head>
<body>
  <main class="canvas">
    <section class="label bottle-label" aria-label="Serum bottle label">
      <h1 class="brand-name">Fernleigh Vale<br>Organics</h1>
      <div class="rule"></div>
      <p class="variant">Nine Moons</p>
      <p class="product-name">Ultimate Anti-Aging Cream</p>
      <div class="details">
        <p>For Dry &amp; Mature Skin</p>
        <p>Organic &amp; Palm Oil-Free</p>
        <p class="volume">100 ml.</p>
      </div>
    </section>

    <section class="label carton-panel" aria-label="Carton front panel">
      <h2 class="brand-name">Fernleigh Vale<br>Organics</h2>
      <div class="rule top-rule"></div>
      <p class="variant">Nine Moons</p>
      <p class="product-name">Ultimate Anti-Aging Cream</p>
      <div class="rule bottom-rule"></div>
      <div class="details">
        <p>For Dry &amp; Mature Skin</p>
        <p>Organic &amp; Palm Oil-Free</p>
        <p class="volume">100 ml.</p>
      </div>
    </section>
  </main>
</body>
</html>
```